Winery Section 199

We need a flyer design for our Accounting Firm that details the benefits of Internal Revenue Code Section 199. This will be marketed to Wineries and Vineyard Farmers We would like to see designs that are bold and utilize our logo and vineyard/winery type symbols colors.

SEE NEW COPY

Target Market(s)

US based wineries and vineyards, Targeting the owners of these companies

Industry/Entity Type

Accounting

Font styles to use
Decorative

Requirements
Must have
• one page - would like to be able to embed into email if possible.
I attached a bunch of logo files only because I don't know which type you need
Nice to have
• see the wording I attached, this is what I would like it to say in general - ok for you to edit if you like. (file 5)

```html
<!DOCTYPE html>
<html lang="en">
<head>
<meta charset="utf-8">
<title>Section 199 Deduction Flyer</title>
<link href="https://fonts.googleapis.com/css2?family=Noto+Sans:wght@400;700&display=swap" rel="stylesheet">
<style>
  :root {
    --parchment: #efe2c4;
    --parchment-dark: #dcc69c;
    --ink-brown: #4a3420;
    --banner-red: #8c1d1b;
    --banner-line: #e9cfa0;
    --white: #ffffff;
    --body-ink: #2b2016;
  }
  html, body { margin: 0; padding: 0; overflow: hidden; }
  body { width: 931px; height: 1200px; background: var(--parchment); }
  .flyer {
    position: relative; width: 931px; height: 1200px; overflow: hidden;
    background: radial-gradient(ellipse at 60% 40%, #f6ecd6 0%, var(--parchment) 55%, var(--parchment-dark) 100%);
    font-family: "Noto Sans", sans-serif; color: var(--ink-brown);
  }
  .vineyard-photo {
    position: absolute; left: 0; top: 0; width: 931px; height: 210px;
    background: linear-gradient(180deg, #e9a640 0%, #c98a3a 22%, #8aa23c 48%, #6f9a2a 75%, #a9b85a 100%);
  }
  .headline {
    position: absolute; left: 0; top: 262px; width: 931px; margin: 0;
    text-align: center; font-weight: 400; font-size: 47px; line-height: 56px;
    color: var(--ink-brown);
  }
  .banner { position: absolute; left: 0; top: 0; width: 931px; height: 1200px; }
  .banner-flourish {
    position: absolute; left: 800px; top: 465px; width: 131px; height: 320px;
    background: linear-gradient(135deg, rgba(233,207,160,0.55), rgba(233,207,160,0.12));
  }
  .still-life-photo {
    position: absolute; left: 0; top: 450px; width: 330px; height: 750px;
    background: linear-gradient(160deg, #c9d88a 0%, #7a5632 30%, #5a3d22 55%, #2f2418 75%, #b89a66 100%);
  }
  .banner-text {
    position: absolute; left: 333px; top: 540px; width: 480px; margin: 0;
    text-align: center; color: var(--white); font-size: 37px; line-height: 52px;
  }
  .banner-text strong { font-weight: 700; font-size: 48px; }
  .pitch {
    position: absolute; left: 387px; top: 770px; width: 470px; margin: 0;
    font-size: 18.5px; line-height: 27px; color: var(--body-ink);
  }
  .call {
    position: absolute; left: 504px; top: 915px; margin: 0;
    font-weight: 700; font-size: 31px; line-height: 42px; color: var(--ink-brown);
  }
  .email {
    position: absolute; left: 504px; top: 1007px; margin: 0;
    font-size: 18px; color: var(--body-ink);
  }
  .firm-name {
    position: absolute; left: 504px; top: 1058px; margin: 0;
    font-weight: 700; font-size: 30px; line-height: 40px; color: var(--ink-brown);
  }
</style>
</head>
<body>
<div class="flyer">
  <div class="vineyard-photo" role="img" aria-label="Photograph of rolling vineyard rows under a golden sunset sky"></div>

  <h1 class="headline">Have you made the decision to<br>keep jobs in the US by hiring<br>here in the United States?</h1>

  <svg class="banner" viewBox="0 0 931 1200" aria-hidden="true">
    <polygon points="200,538 931,458 931,728 200,778" fill="var(--banner-red)"/>
    <line x1="200" y1="552" x2="931" y2="472" stroke="var(--banner-line)" stroke-width="3"/>
    <line x1="200" y1="764" x2="931" y2="714" stroke="var(--banner-line)" stroke-width="3"/>
  </svg>
  <div class="banner-flourish" role="img" aria-label="Decorative gold scroll flourish"></div>

  <div class="still-life-photo" role="img" aria-label="Photograph of a wooden wine barrel, a wine bottle, a glass of white wine and bunches of green grapes"></div>

  <p class="banner-text">You may be unaware<br>of a <strong>9% Deduction</strong><br>the IRS is offering!</p>

  <p class="pitch">We would love to meet with you and explain how your profitable company can pay less taxes, and claim refunds from previous years with this outstanding deduction.</p>

  <p class="call">Call Marian Hollis<br>at 555-014-2368</p>
  <p class="email">mhollis@westfallridge.example</p>

  <p class="firm-name">Westfall Ridge Accounting</p>
</div>
</body>
</html>
```